Velora Aesthetica

Medical doctor providing aesthetic medicine

* Double sided card
* Logo to be on card
Other details:
* Dr. Mirela Kostvan, BSc, MBChB, CCFP
* #214-215, 27903 83 Ave, Surrey, BC, V2T 4K7
* 604-718-2943
* info@veloraclinic.ca
* www.veloraclinic.ca

Industry/Entity Type

Medical / Health & Beauty

Contact Information for Business Card

see 'Project Description'

Colors
0054AA
0677BA
7BADD7
CADEEF
E8F1F8
FFF300
FFF600
FEFA6F
FFFEC7
FFFEE8

Requirements
Must have
• Modern, high-end design

```html
<!DOCTYPE html>
<html lang="en">
<head>
<meta charset="utf-8">
<title>Velora Aesthetica – Business Card</title>
<link href="https://fonts.googleapis.com/css2?family=Lato:wght@400;700&family=Montserrat:wght@500&display=swap" rel="stylesheet">
<style>
  :root {
    --page: #ffffff;
    --stage: #e6e7e9;
    --card-front: #fdfdfd;
    --card-back: #23405f;
    --gold: #dcb22b;
    --ink: #333333;
    --brand-dark: #141414;
    --white: #ffffff;
    --rule: #3a3a3a;
  }
  * { margin: 0; padding: 0; box-sizing: border-box; }
  html, body { width: 1030px; height: 1200px; overflow: hidden; background: var(--page); }
  .stage {
    position: absolute; left: 12px; top: 12px; width: 1006px; height: 1176px;
    background: var(--stage);
  }
  .card {
    position: absolute; width: 856px; height: 489px;
    box-shadow: 0 8px 26px rgba(0,0,0,0.22);
  }
  .card--front { left: 70px; top: 61px; background: var(--card-front); }
  .card--back { left: 61px; top: 595px; background: var(--card-back); }

  .brand {
    font-family: "Montserrat", sans-serif; font-weight: 500;
    text-transform: uppercase; text-align: center; letter-spacing: 0.28em;
    line-height: 1.35;
  }
  .card--front .brand {
    position: absolute; left: 60px; width: 340px; top: 200px;
    font-size: 30px; color: var(--brand-dark);
  }
  .card--back .brand {
    position: absolute; left: 0; width: 100%; top: 190px;
    font-size: 46px; color: var(--white);
  }

  .divider {
    position: absolute; left: 440px; top: 110px; width: 2px; height: 270px;
    background: linear-gradient(to bottom, rgba(58,58,58,0.1), var(--rule) 20%, var(--rule) 80%, rgba(58,58,58,0.1));
  }
  .details { position: absolute; left: 481px; top: 116px; font-family: "Lato", sans-serif; color: var(--ink); }
  .doctor-name { font-size: 33px; font-weight: 700; color: var(--gold); line-height: 1.1; }
  .credentials { font-size: 20px; margin-top: 8px; }
  .contacts { list-style: none; margin-top: 24px; }
  .contact { display: flex; align-items: flex-start; font-size: 20px; line-height: 1.3; margin-bottom: 9px; }
  .contact svg { width: 20px; height: 20px; flex: none; margin-right: 20px; margin-top: 2px; fill: var(--gold); }
  .contact--address { margin-top: 12px; }
</style>
</head>
<body>
<div class="stage">
  <section class="card card--front">
    <div class="brand">Velora<br>Aesthetica</div>
    <div class="divider"></div>
    <div class="details">
      <h1 class="doctor-name">Dr. Mirela Kostvan,</h1>
      <p class="credentials">BSc, MBChB, CCFP</p>
      <ul class="contacts">
        <li class="contact">
          <svg viewBox="0 0 24 24" aria-hidden="true"><path d="M6.6 10.8c1.4 2.8 3.8 5.1 6.6 6.6l2.2-2.2c.3-.3.7-.4 1-.2 1.1.4 2.3.6 3.6.6.6 0 1 .4 1 1V20c0 .6-.4 1-1 1C10.6 21 3 13.4 3 4c0-.6.4-1 1-1h3.5c.6 0 1 .4 1 1 0 1.3.2 2.5.6 3.6.1.3 0 .7-.2 1L6.6 10.8z"/></svg>
          <span>604-718-2943</span>
        </li>
        <li class="contact">
          <svg viewBox="0 0 24 24" aria-hidden="true"><path d="M12 2a10 10 0 100 20 10 10 0 000-20zm6.9 6h-2.9a15.7 15.7 0 00-1.4-3.6A8 8 0 0118.9 8zM12 4c.8 1.2 1.5 2.5 1.9 4h-3.8c.4-1.5 1.1-2.8 1.9-4zM4.3 14a8.2 8.2 0 010-4h3.4a16.5 16.5 0 000 4H4.3zm.8 2h2.9c.3 1.3.8 2.5 1.4 3.6A8 8 0 015.1 16zM8 8H5.1a8 8 0 014.3-3.6C8.8 5.5 8.3 6.7 8 8zm4 12c-.8-1.2-1.5-2.5-1.9-4h3.8c-.4 1.5-1.1 2.8-1.9 4zm2.3-6H9.7a14.7 14.7 0 010-4h4.6a14.7 14.7 0 010 4zm.3 5.6c.6-1.1 1.1-2.3 1.4-3.6h2.9a8 8 0 01-4.3 3.6zm1.7-5.6a16.5 16.5 0 000-4h3.4a8.2 8.2 0 010 4h-3.4z"/></svg>
          <span>www.veloraclinic.ca</span>
        </li>
        <li class="contact">
          <svg viewBox="0 0 24 24" aria-hidden="true"><path d="M2 5h20v14H2V5zm2 2v.5l8 5.5 8-5.5V7l-8 5.5L4 7z"/></svg>
          <span>info@veloraclinic.ca</span>
        </li>
        <li class="contact contact--address">
          <svg viewBox="0 0 24 24" aria-hidden="true"><path d="M12 2a7 7 0 00-7 7c0 5.2 7 13 7 13s7-7.8 7-13a7 7 0 00-7-7zm0 9.5A2.5 2.5 0 1112 6.5a2.5 2.5 0 010 5z"/></svg>
          <span>#214-215, 27903 83 Ave,<br>Surrey, BC, V2T 4K7</span>
        </li>
      </ul>
    </div>
  </section>

  <section class="card card--back">
    <div class="brand">Velora<br>Aesthetica</div>
  </section>
</div>
</body>
</html>
```